Varnek Group Business Card

Varnek Group — Business Card Design Brief
Overview
Design a double-sided business card for Varnek Group that highlights our two service arms: Varnek Communications (telecommunications) and Varnek Energy (business energy solutions). The card should feel smart and stand out when handed to clients.

Objectives
Showcase our areas of specialty clearly.
Reflect the overall Varnek / Varnek Group brand while acknowledging both arms.
Explore using both logos (Communications + Energy) or one unified logo, depending on the design.

Deliverables
One double-sided business card design (front + back).

Content & Copy
Front (preferred): Logo: Varnek / Varnek Group
Descriptor: Business Communications | Business Energy
Back:My contact details and company details
Core products: Business Mobile • Telephony • Internet • Business Energy Solutions

Brand & Visual Direction
We have a group logo currently tailored more toward telecoms, plus a separate Varnek Energy logo.
Please explore layouts that use both logos or just one, whichever works best.
Color: I wouldn't mind seeing an option using our the Blue/Purple gradient from our website (varnek-example.co.uk), but also open to non-gradient approaches and other colours..

Overall look: Smart, modern, and distinctive.
Format & Print Specs
Double-sided business card format. (Use a standard size

Must-Haves
Front: Varnek wording or Varnek Group wording with atleast 1 logo also on front “Business Communications | Business Energy.”

Back: Contact + company details and core products.
A design that stands out while remaining professional.

Nice-to-Have Options
A gradient version using our site’s Blue/Purple gradient.
A non-gradient version.
A dual-logo treatment versus a single-logo treatment.

Thanks
Dominic

```html
<!DOCTYPE html>
<html lang="en">
<head>
<meta charset="utf-8">
<title>Varnek Group Business Card</title>
<link href="https://fonts.googleapis.com/css2?family=Poppins:wght@400;500;600;800&display=swap" rel="stylesheet">
<style>
  :root {
    --stage: #2b2c30;
    --card-navy: #1d1772;
    --card-navy-light: #2a2596;
    --brand-blue: #2b8fe6;
    --brand-cyan: #1fb5e8;
    --brand-green: #5fbf2a;
    --text-white: #ffffff;
  }
  * { margin: 0; padding: 0; box-sizing: border-box; }
  html, body { width: 1200px; height: 952px; overflow: hidden; }
  body {
    background: var(--stage);
    font-family: "Poppins", sans-serif;
    color: var(--text-white);
    display: flex;
    flex-direction: column;
    align-items: center;
    justify-content: center;
    gap: 30px;
  }
  .card {
    position: relative;
    width: 760px;
    height: 434px;
    background: var(--card-navy);
    overflow: hidden;
    box-shadow: 0 12px 30px rgba(0,0,0,0.45);
  }

  /* Front */
  .card-front .network-backdrop {
    position: absolute;
    inset: 0;
    background:
      radial-gradient(ellipse 55% 60% at 60% 45%, rgba(60,70,200,0.35), transparent 70%),
      radial-gradient(ellipse 40% 45% at 20% 70%, rgba(55,60,190,0.25), transparent 70%),
      linear-gradient(135deg, var(--card-navy) 0%, var(--card-navy-light) 100%);
  }
  .front-lockup {
    position: absolute;
    left: 50%;
    top: 44%;
    transform: translate(-50%, -50%);
    display: flex;
    align-items: center;
    gap: 18px;
  }
  .brand-dot {
    width: 58px;
    height: 58px;
    border-radius: 50%;
    background: var(--brand-blue);
  }
  .brand-name {
    font-weight: 800;
    font-size: 84px;
    letter-spacing: 2px;
    line-height: 1;
  }
  .descriptor {
    position: absolute;
    left: 0;
    right: 0;
    bottom: 70px;
    text-align: center;
    font-weight: 500;
    font-size: 16px;
    letter-spacing: 1.5px;
    text-transform: uppercase;
  }
  .descriptor .sep { color: var(--brand-cyan); margin: 0 12px; }

  /* Back */
  .back-lockup {
    position: absolute;
    left: 60px;
    top: 46px;
    display: flex;
    align-items: center;
    gap: 12px;
  }
  .back-lockup .brand-dot { width: 34px; height: 34px; background: var(--brand-green); }
  .back-lockup .brand-name { font-size: 46px; }
  .contact-list {
    position: absolute;
    left: 60px;
    top: 140px;
    list-style: none;
    font-size: 15px;
    line-height: 1.35;
  }
  .contact-list li {
    display: flex;
    align-items: flex-start;
    gap: 12px;
    margin-bottom: 12px;
  }
  .contact-icon {
    flex: none;
    width: 22px;
    height: 22px;
    border-radius: 3px;
    background: var(--brand-blue);
    display: flex;
    align-items: center;
    justify-content: center;
  }
  .contact-icon.is-location { background: var(--brand-green); }
  .contact-icon svg { width: 14px; height: 14px; fill: var(--text-white); }
  .person {
    position: absolute;
    right: 60px;
    top: 170px;
    text-align: right;
  }
  .person-name {
    font-weight: 600;
    font-size: 30px;
    letter-spacing: 2px;
    color: var(--brand-blue);
    text-transform: uppercase;
  }
  .person-name .surname { font-weight: 800; }
  .person-role {
    font-size: 22px;
    margin-top: 2px;
  }
  .person-rule {
    width: 100px;
    height: 2px;
    background: var(--text-white);
    margin: 10px 0 0 auto;
  }
  .product-line {
    position: absolute;
    left: 60px;
    right: 60px;
    bottom: 40px;
    padding-top: 16px;
    border-top: 1px solid rgba(255,255,255,0.18);
    text-align: center;
    font-weight: 500;
    font-size: 14px;
    letter-spacing: 1px;
    text-transform: uppercase;
  }
  .product-line .sep { color: var(--brand-cyan); margin: 0 6px; }
</style>
</head>
<body>

  <section class="card card-front" aria-label="Business card front">
    <div class="network-backdrop" role="img" aria-label="Faint world map with dotted connection lines"></div>
    <div class="front-lockup">
      <span class="brand-dot"></span>
      <span class="brand-name">VARNEK</span>
    </div>
    <p class="descriptor">
      Business Communications<span class="sep">|</span>Business Energy
    </p>
  </section>

  <section class="card card-back" aria-label="Business card back">
    <div class="back-lockup">
      <span class="brand-dot"></span>
      <span class="brand-name">VARNEK</span>
    </div>

    <ul class="contact-list">
      <li>
        <span class="contact-icon is-location">
          <svg viewBox="0 0 24 24"><path d="M12 2a7 7 0 0 0-7 7c0 5.2 7 13 7 13s7-7.8 7-13a7 7 0 0 0-7-7zm0 9.5A2.5 2.5 0 1 1 12 6.5a2.5 2.5 0 0 1 0 5z"/></svg>
        </span>
        <span>218 Elmfield Avenue<br>Leeds, LS7 4QP</span>
      </li>
      <li>
        <span class="contact-icon">
          <svg viewBox="0 0 24 24"><path d="M6.6 10.8a15.1 15.1 0 0 0 6.6 6.6l2.2-2.2a1 1 0 0 1 1-.25 11.4 11.4 0 0 0 3.6.57 1 1 0 0 1 1 1V20a1 1 0 0 1-1 1A17 17 0 0 1 3 4a1 1 0 0 1 1-1h3.5a1 1 0 0 1 1 1c0 1.25.2 2.45.57 3.570a1 1 0 0 1-.25 1z"/></svg>
        </span>
        <span>+44 113 496 0721</span>
      </li>
      <li>
        <span class="contact-icon">
          <svg viewBox="0 0 24 24"><path d="M3 5h18v14H3zm2 2v.5l7 4.5 7-4.5V7zm0 2.9V17h14V9.9l-7 4.5z"/></svg>
        </span>
        <span>hello@varnek-example.co.uk</span>
      </li>
      <li>
        <span class="contact-icon">
          <svg viewBox="0 0 24 24"><path d="M5 3l14 7-6 2-2 6z"/></svg>
        </span>
        <span>www.varnek-example.co.uk</span>
      </li>
    </ul>

    <div class="person">
      <p class="person-name">Colin R. <span class="surname">Hartwell</span></p>
      <p class="person-role">Managing Director</p>
      <div class="person-rule"></div>
    </div>

    <p class="product-line">
      Business Mobile<span class="sep">•</span>Telephony<span class="sep">•</span>Internet<span class="sep">•</span>Business Energy Solutions
    </p>
  </section>

</body>
</html>
```